Corvo Pizza & Pasta dual-restaurant promotional flyer

I would like to do a tri-fold flyer to promote my two restaurants located close to each other and help concierges understand the subtle differences between them. I have done a mock in powerpoint but it is 300+MB so i took pics of my mock to attach and will attach the separate pictures and text. i would like it put into a proper flyer template and get help to clean up the design, particularly the flyer header which should show either i) our CORVO PIZZA and CORVO PASTA logo or ii) show CORVO logo and then have the words Corvo Pizza Corvo Pasta below it (in non-logo). I have the logo files in vector and pdf too if that is better. I need help to photoshop the logos to work with the flyer and clean up overall design. The pages which shows the restaurant contact details is also a little hard to read in the current layout. Open to all changes.

Industry/Entity Type

Restaurant

Requirements
Must have
• Front page - must feature both logos and both restaurants photos (that i show on my uploaded draft flyer)
• All photos must be used
Nice to have
• I have uploaded a draft flyer of what i am trying to achieve
Should not have
• The feel should be warm and personable.

```html
<!DOCTYPE html>
<html lang="en">
<head>
<meta charset="utf-8">
<title>Corvo Pizza &amp; Pasta – Inside Spread</title>
<link href="https://fonts.googleapis.com/css2?family=Noto+Serif:ital,wght@0,400;0,700;1,400;1,700&family=Roboto+Slab:wght@700&display=swap" rel="stylesheet">
<style>
  :root {
    --stage: #d5d7d9;
    --panel: #524842;
    --ink: #f4f0ec;
    --green: #22a04f;
    --blue: #2aa2da;
    --orange: #e5822f;
    --frame: #ffffff;
    --rule: #9a8f88;
  }
  * { margin: 0; padding: 0; box-sizing: border-box; }
  html, body { width: 1200px; height: 1000px; overflow: hidden; background: var(--stage); }
  body { position: relative; font-family: "Noto Serif", Georgia, serif; color: var(--ink); }
  .spread { position: absolute; left: 80px; top: 98px; width: 1040px; height: 804px; background: var(--panel); box-shadow: 0 1px 4px rgba(0,0,0,.15); }
  .block { position: absolute; }
  .section-title { font-family: "Roboto Slab", Georgia, serif; font-weight: 700; font-size: 18px; line-height: 22px; }
  .section-title.food { color: var(--green); }
  .section-title.drinks { color: var(--orange); }
  .body-copy { font-size: 12.6px; line-height: 15.6px; }
  .body-copy p + p { margin-top: 15.6px; }
  .body-copy b { font-weight: 700; }
  .drinks-copy { font-size: 14px; line-height: 18.6px; }
  .photo { position: absolute; border: 3px solid var(--frame); }
  .caption { font-size: 12.6px; line-height: 17px; font-style: italic; }
  .caption .dish { color: var(--green); font-weight: 700; }
  .rule { position: absolute; left: 446px; width: 310px; border-top: 1px dotted var(--rule); }
  .quote { position: absolute; left: 446px; top: 330px; width: 310px; text-align: center; color: var(--blue); font-weight: 700; font-size: 16px; line-height: 26px; }
  .quote .mark { font-family: "Roboto Slab", Georgia, serif; font-size: 34px; line-height: 10px; vertical-align: -6px; }
  .quote-credit { position: absolute; left: 446px; top: 442px; width: 310px; text-align: center; color: var(--blue); font-size: 10.5px; }
  .wine-list { font-size: 14px; line-height: 18.6px; }
  .wine-list .head { font-weight: 700; }
  .beer-title { font-weight: 700; font-size: 14px; line-height: 18px; }
  .beer-list { font-size: 14px; line-height: 18px; margin-top: 9px; }
</style>
</head>
<body>
<main class="spread">

  <!-- Left column -->
  <h2 class="block section-title food" style="left:27px;top:20px;">OUR FOOD</h2>
  <div class="block body-copy" style="left:27px;top:41px;width:310px;">
    <p>We are famed for our huge selection of white &amp; red pizzas, among which our <b>Pizza Corvo Pizza, Mascarpone Pizza and Pizza Apetitosa</b> are some of the most popular choices. Our pizza dough is <b>handmade fresh daily</b> and topped with only <b>the freshest ingredients.</b><br>For instance, a discerning palate will tell that we only use <b>top-grade salami.</b></p>
    <p>We can go on for hours about our pizzas but there are mainly other deserving items on our menu like our <b>Risotto al Funghi, Rigatoni Sicilliana and Parpadelle Boscoiala.</b><br>The pizzeria also features pasta dishes but Corvo Pasta's menu is deiliberately more extensive with a wide selection of seafood and meat options as well. <b>Corvo Pizza's pies can also be ordered at Corvo Pasta.</b></p>
    <p>If you woud like something sweet to finish, our <b>creamy tiramisu</b> and our <b>vanilla bean pannacotta</b> never fail to deliver.</p>
  </div>

  <div class="photo" role="img" aria-label="Photo of linguine frutti di mare with prawns and clams" style="left:43px;top:405px;width:260px;height:144px;background:linear-gradient(135deg,#f3efe9 0%,#d9683a 40%,#c0512c 65%,#efe9e2 100%);"></div>
  <p class="block caption" style="left:27px;top:555px;width:300px;"><span class="dish">LINGUINE FRUTTI DI MARE</span> - a tangy tomato based house favourite or try it ......style.</p>

  <div class="photo" role="img" aria-label="Photo of handmade pappardelle boscaiola with mushrooms" style="left:43px;top:600px;width:260px;height:144px;background:linear-gradient(135deg,#efe7dc 0%,#b56a3e 45%,#8a4a2b 70%,#e9e2d8 100%);"></div>
  <p class="block caption" style="left:27px;top:751px;width:300px;"><span class="dish">HANDMADE PARPADELLE BOSCOIALA -</span> always a winner</p>

  <!-- Middle column -->
  <div class="photo" role="img" aria-label="Photo of spinach salad with feta, orange and pine nuts" style="left:391px;top:0;width:258px;height:166px;background:linear-gradient(135deg,#e9ece8 0%,#3f7a2e 40%,#e49a3a 60%,#2d5a22 80%,#f2f2f0 100%);"></div>
  <p class="block caption" style="left:360px;top:174px;width:340px;"><span class="dish">INSALATE DI SPINACI</span> - a light and refreshing starter.</p>

  <div class="rule" style="top:211px;left:366px;"></div>
  <p class="quote" style="left:366px;top:232px;"><span class="mark">“</span> You must go to Corvo Pizza, they have REALLY GOOD ITALIAN FOOD but DO NOT BLOG about it! <span class="mark">”</span></p>
  <p class="quote-credit" style="left:366px;top:344px;">(Dana Wren a.k.a Celebrity Blogger Fork &amp; Fable)</p>
  <div class="rule" style="top:372px;left:366px;"></div>

  <p class="block caption" style="left:360px;top:396px;width:340px;"><span class="dish">BACON SICILIAN BOAT PIZZA</span> - that is not commonly found in Singapore.</p>
  <div class="photo" role="img" aria-label="Close-up photo of cured ham draped over a boat-shaped pizza" style="left:399px;top:440px;width:259px;height:364px;background:radial-gradient(ellipse at 55% 50%,#a8453f 0%,#8e3a35 45%,#c9a8a0 80%,#ece8e6 100%);"></div>

  <!-- Right column -->
  <div class="photo" role="img" aria-label="Photo of Pizza Corvo Pizza with ricotta, salami and spinach" style="left:736px;top:24px;width:260px;height:145px;background:radial-gradient(ellipse at 50% 60%,#e9d6a8 0%,#b8532f 45%,#d9a15a 70%,#6d7d8a 100%);"></div>
  <p class="block caption" style="left:709px;top:176px;width:310px;"><span class="dish">PIZZA CORVO PIZZA</span> - our signature pizza in a scrumptuous ricotta salami spinach combination.</p>

  <div class="photo" role="img" aria-label="Photo of grilled prawns and calamari with lemon" style="left:736px;top:220px;width:260px;height:144px;background:linear-gradient(135deg,#f3ece2 0%,#e9c9a8 35%,#d0623a 55%,#3e7a2c 80%,#f1d24a 100%);"></div>
  <p class="block caption" style="left:709px;top:375px;width:310px;"><span class="dish">GRIGLATA GAMBERI A CALAMARI</span> - one of the many mains to choose from at Corvo Pasta.</p>

  <h2 class="block section-title drinks" style="left:709px;top:432px;">OUR WINES &amp; BEERS</h2>
  <div class="block drinks-copy" style="left:709px;top:459px;width:325px;">
    We offer a carefully <b>curated selection of well-known Italian</b> and <b>new world wines</b> at excellent value and take pride in offering really good quality, generous house pours.<br>For those who prefer <b>beers and spirits,</b> there is also a wide selection so do drop in for a early drink by the river!
  </div>

  <div class="block wine-list" style="left:709px;top:601px;width:325px;">
    <div class="head">HOUSE POURS......................Gls / Carafe / Bot</div>
    <div>Montepulciano, Colle Rosso..12 / &nbsp;&nbsp; 30 &nbsp;&nbsp; / 55</div>
    <div>Chianti Classico,</div>
    <div>Poggio Alto...............................15 / &nbsp;&nbsp; 41 &nbsp;&nbsp; / 74</div>
    <div>Pinot Grigio, Casa Luna..........12 / &nbsp;&nbsp; 30 &nbsp;&nbsp; / 55</div>
    <div>Sauvignon Blanc.</div>
    <div>Stone Creek Marlborough.......15 / &nbsp;&nbsp; 39 &nbsp;&nbsp; / 72</div>
  </div>

  <div class="block" style="left:709px;top:749px;width:325px;">
    <div class="beer-title">BEERS BY BOTTLE</div>
    <div class="beer-list">Ferrano, Witbrook, Sorano, Valbrea, Lionel</div>
  </div>

</main>
</body>
</html>
```